Conceptual Model Diagram for Replacing Medication with Behavior to Support Weight Loss Maintenance

Design a figure of a conceptual model that needs to be inserted into a word document for a QDV grant. This conceptual model illustrates how behavioral strategies can replace the regulatory functions lost after AOM discontinuation. The intervention targets three core vulnerabilities—appetite resurgence, metabolic inflexibility, and suboptimal mindstate—through the domains of Food, Physical Activity, and Mind. Sustained weight loss maintenance occurs at the intersection of these domains. The intervention is delivered within a design framework that makes behaviors easier to perform, aligns them with identity, and reinforces them through virtual support and community, ensuring real-world feasibility and long-term adherence.
Target Market(s)
QDV reviewers
Industry/Entity Type
academic
Font styles to use
Other font styles liked:
- arial
Requirements
Must have
- see my attached description

```html
<!DOCTYPE html>
<html lang="en">
<head>
<meta charset="utf-8">
<title>Conceptual Model for Replacing Medication with Behavior to Support Weight Loss Maintenance</title>
<link rel="stylesheet" href="https://fonts.googleapis.com/css2?family=Arimo:wght@400;700&display=swap">
<style>
  :root {
    --paper: #ffffff;
    --ink: #1f1f1f;
    --ink-soft: #4a4a4a;
    --ring: #8a8a8a;
    --ring-line: #6d6d6d;
    --domain-fill: #c9c9c9;
    --core-fill: #ffffff;
  }
  html, body {
    margin: 0;
    padding: 0;
    width: 1200px;
    height: 2400px;
    overflow: hidden;
    background: var(--paper);
  }
  .canvas {
    position: relative;
    width: 1200px;
    height: 2400px;
    font-family: "Arimo", Arial, sans-serif;
    color: var(--ink);
  }
  .model {
    position: absolute;
    left: 100px;
    top: 650px;
    width: 1000px;
    height: 1000px;
  }
  .model-caption {
    position: absolute;
    left: 0;
    right: 0;
    top: 1700px;
    margin: 0;
    text-align: center;
    font-size: 30px;
    font-weight: 700;
    line-height: 1.3;
    color: var(--ink);
  }
  .frame-label { font-size: 22px; fill: var(--ink); }
  .ring-label { font-size: 24px; fill: var(--ink); font-weight: 700; }
  .inner-label { font-size: 20px; fill: var(--ink); }
  .domain-label { font-size: 34px; font-weight: 700; fill: var(--ink); }
  .risk-label { font-size: 18px; fill: var(--ink-soft); }
  .core-label { font-size: 17px; font-weight: 700; fill: var(--ink); }
</style>
</head>
<body>
<main class="canvas">
  <svg class="model" viewBox="0 0 1000 1000" aria-label="Conceptual model diagram">
    <defs>
      <path id="path-outer" d="M500,900 A400,400 0 1 1 500,100 A400,400 0 1 1 500,900"/>
      <path id="path-ring" d="M500,842 A342,342 0 1 1 500,158 A342,342 0 1 1 500,842"/>
      <path id="path-ring-top" d="M158,500 A342,342 0 0 1 842,500"/>
      <path id="path-outer-bottom" d="M90,500 A410,410 0 0 0 910,500"/>
      <path id="path-inner-bottom" d="M205,500 A295,295 0 0 0 795,500"/>
      <path id="path-food" d="M253,425 A157,157 0 0 1 410,268"/>
      <path id="path-activity" d="M590,268 A157,157 0 0 1 747,425"/>
    </defs>

    <!-- outer support frame -->
    <circle class="support-frame" cx="500" cy="500" r="425" fill="none" stroke="var(--ring-line)" stroke-width="2" stroke-dasharray="10 8"/>
    <text class="frame-label"><textPath href="#path-outer" startOffset="31%" text-anchor="middle">Virtual Support and Social Connection</textPath></text>
    <text class="frame-label"><textPath href="#path-outer-bottom" startOffset="73%" text-anchor="middle">accessibility, community, shared accountability</textPath></text>

    <!-- design framework ring -->
    <circle class="framework-ring" cx="500" cy="500" r="350" fill="none" stroke="var(--ring)" stroke-width="40"/>
    <text class="ring-label"><textPath href="#path-ring-top" startOffset="50%" text-anchor="middle">Make it Easy</textPath></text>
    <text class="ring-label"><textPath href="#path-ring" startOffset="64%" text-anchor="middle">Align with Identity</textPath></text>
    <text class="ring-label"><textPath href="#path-ring" startOffset="16%" text-anchor="middle">reinforcement, feedback, motivation</textPath></text>

    <!-- inner behavior boundary -->
    <circle class="behavior-boundary" cx="500" cy="500" r="305" fill="none" stroke="var(--ring-line)" stroke-width="2"/>
    <text class="inner-label"><textPath href="#path-inner-bottom" startOffset="50%" text-anchor="middle">habits, routines, environment, low friction</textPath></text>

    <!-- domains -->
    <g class="domains" style="mix-blend-mode:multiply">
      <circle cx="410" cy="425" r="140" fill="var(--domain-fill)" fill-opacity="0.6" stroke="var(--ring-line)" stroke-width="2"/>
      <circle cx="590" cy="425" r="140" fill="var(--domain-fill)" fill-opacity="0.6" stroke="var(--ring-line)" stroke-width="2"/>
      <circle cx="500" cy="578" r="140" fill="var(--domain-fill)" fill-opacity="0.6" stroke="var(--ring-line)" stroke-width="2"/>
    </g>
    <text class="domain-label" x="365" y="410" text-anchor="middle">Food</text>
    <text class="domain-label" x="637" y="398" text-anchor="middle">Physical</text>
    <text class="domain-label" x="637" y="438" text-anchor="middle">Activity</text>
    <text class="domain-label" x="500" y="660" text-anchor="middle">Mind</text>

    <!-- vulnerabilities -->
    <text class="risk-label"><textPath href="#path-food" startOffset="50%" text-anchor="middle">Appetite Resurgence</textPath></text>
    <text class="risk-label"><textPath href="#path-activity" startOffset="50%" text-anchor="middle">Metabolic Inflexibility</textPath></text>
    <line x1="500" y1="718" x2="500" y2="734" stroke="var(--ink)" stroke-width="2"/>
    <text class="risk-label" x="500" y="752" text-anchor="middle">Suboptimal Mindstate</text>

    <!-- core outcome -->
    <rect x="432" y="446" width="136" height="64" rx="8" fill="var(--core-fill)" fill-opacity="0.85" stroke="var(--ring-line)" stroke-width="1.5"/>
    <text class="core-label" x="500" y="470" text-anchor="middle">Sustained</text>
    <text class="core-label" x="500" y="488" text-anchor="middle">Weight Loss</text>
    <text class="core-label" x="500" y="506" text-anchor="middle">Maintenance</text>
  </svg>

  <h1 class="model-caption">Conceptual Model for Replacing Medication with<br>Behavior to Support Weight Loss Maintenance</h1>
</main>
</body>
</html>
```